Peanut Butter for Dogs - Label

Dear Designers,

Our company develops natural & innovative products aimed at enhancing animal (cat & dog) well-being. The company focuses on producing high-end, ethically sourced products that naturally soothe pets, improving their quality of life.

We are currently developing a new CBD-enriched Peanut Butter product for dogs, and we are looking for some label designs that follow our brand image & brand identity.

-> Please see full brief PDF file attached.

Target Market(s)

European Market (French Speaking)

Industry/Entity Type

Pet Food

Font styles to use
Other font styles liked:
• Please see brand kit in PDF brief

Colors

Designer to choose colors to be used in the design.

Requirements
Must have
• Please see brief PDF file attached
Nice to have
Should not have

```html
<!DOCTYPE html>
<html lang="fr">
<head>
<meta charset="utf-8">
<title>Verdalys – Peanut Butter for Dogs – Étiquette</title>
<link rel="stylesheet" href="https://fonts.googleapis.com/css2?family=Cinzel:wght@600&family=Questrial&display=swap">
<style>
  :root {
    --backdrop: #7a5140;
    --label-light: #f8eab8;
    --label-mid: #f0d9a0;
    --label-edge: #e2c084;
    --forest: #0e3b37;
    --band: #053935;
    --band-text: #f4ecd6;
    --art-light: #c98a4e;
    --art-dark: #3b2a22;
  }
  * { margin: 0; padding: 0; box-sizing: border-box; }
  html, body {
    width: 1200px;
    height: 900px;
    overflow: hidden;
    background: var(--backdrop);
  }
  .canvas {
    position: relative;
    width: 1200px;
    height: 900px;
  }
  .label {
    position: absolute;
    left: 240px;
    top: 81px;
    width: 720px;
    height: 738px;
    background: linear-gradient(90deg, var(--label-edge) 0%, var(--label-mid) 20%, var(--label-light) 50%, var(--label-mid) 80%, var(--label-edge) 100%);
    overflow: hidden;
  }
  .brand {
    position: absolute;
    top: 58px;
    left: 0;
    width: 100%;
    display: flex;
    justify-content: center;
    align-items: center;
    gap: 22px;
  }
  .brand-dot {
    width: 52px;
    height: 52px;
    border-radius: 50%;
    background: var(--forest);
  }
  .brand-name {
    font-family: "Questrial", sans-serif;
    font-size: 74px;
    line-height: 1;
    letter-spacing: 2px;
    color: var(--forest);
  }
  .brand-tagline {
    position: absolute;
    top: 140px;
    left: 76px;
    right: 76px;
    display: flex;
    align-items: center;
    gap: 12px;
    font-family: "Questrial", sans-serif;
    font-size: 21px;
    color: var(--forest);
  }
  .brand-tagline::before,
  .brand-tagline::after {
    content: "";
    height: 2px;
    background: var(--forest);
  }
  .brand-tagline::before { flex: 1.15; }
  .brand-tagline::after { flex: 1; }
  .product-name {
    position: absolute;
    top: 210px;
    width: 100%;
    text-align: center;
    font-family: "Cinzel", serif;
    font-weight: 600;
    font-size: 29px;
    letter-spacing: 1px;
    color: var(--forest);
  }
  .dogs-art {
    position: absolute;
    top: 278px;
    left: 150px;
    width: 434px;
    height: 335px;
    border-radius: 40px 40px 0 0;
    background: linear-gradient(90deg, var(--art-light) 0%, #a8683a 40%, var(--art-dark) 65%, #5a3c2c 100%);
    opacity: 0.85;
  }
  .claim-band {
    position: absolute;
    top: 613px;
    left: 0;
    width: 100%;
    height: 125px;
    background: var(--band);
    display: flex;
    align-items: center;
    justify-content: center;
  }
  .claim {
    font-family: "Cinzel", serif;
    font-weight: 600;
    font-size: 25px;
    letter-spacing: 1px;
    color: var(--band-text);
  }
</style>
</head>
<body>
  <main class="canvas">
    <section class="label">
      <div class="brand">
        <span class="brand-dot"></span>
        <span class="brand-name">VERDALYS</span>
      </div>
      <div class="brand-tagline">For animals</div>
      <h1 class="product-name">PEANUT BUTTER FOR DOGS</h1>
      <div class="dogs-art" role="img" aria-label="Illustration de deux chiens assis côte à côte : un jeune épagneul roux et un bouvier bernois tricolore"></div>
      <div class="claim-band">
        <p class="claim">FRIANDISES APAISANTES</p>
      </div>
    </section>
  </main>
</body>
</html>
```